International IT business needs website revamp.

Velbric Limited would like their current website (www.velbriclimited.example) to be revamped/modernized to reflect up-to-date goods and services. Currently, Velbric is offering a conversational AI workflow platform for both enterprise clients and as a DIY solution for SMBs. This platform is called tmPilot and allows organizations to automate simple and repetitive workflows to drive their operational efficiency. In addition to the solution offering, Velbric Limited also provides professional IT services. With that said, please use www.velbriclimited.example and www.tmpilot.example for reference of current logos and colourways desired. Furthermore, refer to the attached PDF for a general idea of what to include in the site. The final design should be easy to navigate, clear, concise, and emphasize tmPilot as a solution for enterprise clients (while redirecting SMBs to the tmPilot website) looking to automate workflow processes/kickstart their digital transformation journey.
Updates
Coding
Number of Pages Required
5+ page
Font styles to use
Look and feel
Each slider illustrates characteristics of the customer's brand and the style your logo design should communicate.

```html
<!DOCTYPE html>
<html lang="en">
<head>
<meta charset="utf-8">
<title>Velbric Limited – Home</title>
<link href="https://fonts.googleapis.com/css2?family=Poppins:wght@400;500;600;700&display=swap" rel="stylesheet">
<style>
:root{
  --blue:#0a8fd4;
  --blue-dark:#0a5eae;
  --ink:#111;
  --text:#444;
  --muted:#666;
  --pale:#eef6fc;
  --pale-2:#e4f1fa;
  --line:#7a7a7a;
  --star:#f6b21b;
  --white:#fff;
}
*{margin:0;padding:0;box-sizing:border-box}
html,body{width:1200px;height:2875px;overflow:hidden}
body{position:relative;font-family:'Poppins',sans-serif;color:var(--ink);background:var(--white)}
.abs{position:absolute}
/* header */
.site-header{position:absolute;left:0;top:0;width:1200px;height:94px;background:var(--white)}
.brand{position:absolute;display:flex;align-items:center;gap:6px;font-weight:500;color:var(--ink)}
.brand-box{width:38px;height:38px;border:3px solid var(--ink)}
.main-nav{position:absolute;left:414px;top:33px;display:flex;gap:6px;font-size:10.5px;font-weight:500;letter-spacing:.3px;white-space:nowrap}
.main-nav span{padding:7px 9px}
.main-nav .active{border:1.5px solid var(--ink)}
.header-phone{position:absolute;left:816px;top:34px;font-size:16.5px;font-weight:500;display:flex;align-items:center;gap:9px;white-space:nowrap}
/* hero */
.hero{position:absolute;left:0;top:94px;width:1200px;height:472px}
.hero-title{position:absolute;left:266px;top:208px;width:262px;text-align:center;font-size:32px;font-weight:700;line-height:37px;letter-spacing:.5px}
.product-name{position:absolute;left:298px;top:168px;display:flex;align-items:center;gap:8px;font-size:32px;line-height:40px;color:var(--blue);font-weight:400}
.product-name i{width:40px;height:40px;border-radius:50%;background:var(--blue);display:block}
.feature{position:absolute;width:250px}
.feature h3{font-size:13.5px;font-weight:600;margin-bottom:4px}
.feature p{font-size:9.3px;line-height:16px;color:#333}
.feature-icon{position:absolute;width:68px;height:68px;border-radius:50%;background:var(--blue);display:flex;align-items:center;justify-content:center}
.slider-dots{position:absolute;left:574px;top:409px;display:flex;gap:8px}
.slider-dots i{width:12px;height:12px;border:1.5px solid var(--ink);display:block}
.slider-dots i.on{background:var(--ink)}
/* section heads */
.eyebrow{position:absolute;left:0;width:1200px;text-align:center;color:var(--blue);font-size:12px;font-weight:500;letter-spacing:3px}
.section-title{position:absolute;left:0;width:1200px;text-align:center;font-size:32px;font-weight:700}
.services-intro{position:absolute;left:285px;top:714px;width:630px;text-align:center;font-size:9.2px;line-height:15px;color:var(--text)}
.service-card{position:absolute;width:226px;text-align:left}
.service-card h4{font-size:13px;font-weight:600;color:#333;margin-bottom:10px}
.service-card li{list-style:none;font-size:9.3px;line-height:15px;color:#444;padding-left:11px;position:relative;margin-bottom:4px}
.service-card li::before{content:"";position:absolute;left:0;top:5px;width:4px;height:4px;border-radius:50%;background:var(--blue)}
.service-icon{position:absolute;width:55px;height:55px;border-radius:50%;background:linear-gradient(135deg,#18b2ea,var(--blue-dark))}
.center-mark{position:absolute;left:546px;top:908px;width:108px;height:108px;border:9px solid var(--blue);display:flex;align-items:center;justify-content:center;color:var(--blue);font-weight:600;font-size:17px}
/* testimonials */
.testimonials{position:absolute;left:0;top:1161px;width:1200px;height:545px;background:var(--pale)}
.quote-card{position:absolute;top:1323px;width:356px;height:291px;background:var(--white);box-shadow:0 2px 10px rgba(10,80,130,.08);padding:22px 28px}
.quote-mark{font-size:70px;line-height:60px;height:44px;color:var(--blue);font-weight:700;font-family:Georgia,serif}
.quote-card p{font-size:10.4px;line-height:16.2px;color:#444;margin-top:6px}
.quote-card h5{font-size:11.5px;font-weight:600;color:#333;margin-top:14px}
.stars{color:var(--star);font-size:14px;letter-spacing:1px;margin-top:2px}
.carousel-dots{position:absolute;left:583px;top:1659px;display:flex;gap:5px}
.carousel-dots i{width:5px;height:5px;border-radius:50%;background:#9bbfd6;display:block}
.carousel-dots i.on{background:var(--blue)}
/* video */
.video{position:absolute;left:234px;top:1771px;width:732px;height:415px;background:linear-gradient(100deg,#2a2e33,#4a4744 55%,#1d1f22);box-shadow:0 4px 14px rgba(0,0,0,.3)}
.video-brand{position:absolute;left:24px;top:26px;color:#fff;font-size:9px;font-weight:500;display:flex;align-items:center;gap:7px}
.video-brand i{width:13px;height:13px;border:1.5px solid #fff;display:block}
.video-action{position:absolute;top:22px;color:#fff;font-size:9px;font-weight:600;text-align:center;width:60px}
.play{position:absolute;left:340px;top:188px;width:52px;height:40px;border-radius:50%;background:var(--blue)}
.divider-v{position:absolute;left:600px;top:2186px;width:1px;height:292px;background:#e2e2e2}
.logo-block-title{position:absolute;width:380px;text-align:center;font-size:26px;font-weight:700}
.logo-name{position:absolute;width:110px;text-align:center;font-size:22px;font-weight:600;color:var(--blue-dark)}
.to-top{position:absolute;left:583px;top:2478px;width:34px;height:34px;border-radius:50%;background:linear-gradient(135deg,#18b2ea,var(--blue-dark))}
/* footer */
.site-footer{position:absolute;left:0;top:2520px;width:1200px;height:355px}
.footer-about{position:absolute;left:235px;top:2636px;width:232px;font-size:9.3px;line-height:16.2px;color:#333}
.footer-col{position:absolute;top:2594px}
.footer-col h6{font-size:10.8px;font-weight:600;letter-spacing:.3px;position:relative;padding-bottom:9px}
.footer-col h6::after{content:"";position:absolute;left:0;bottom:0;width:22px;height:2px;background:var(--blue)}
.footer-col li{list-style:none;font-size:9.3px;color:#333;line-height:25px}
.footer-col p{font-size:9.3px;color:#333;line-height:16px;margin-top:12px}
.social li{display:flex;align-items:center;gap:8px}
.social i{width:17px;height:17px;border-radius:50%;background:var(--blue);display:block}
.footer-rule{position:absolute;left:234px;top:2808px;width:732px;height:1px;background:#dfe9f0}
.copyright{position:absolute;left:0;top:2838px;width:1200px;text-align:center;font-size:9.3px;color:#333}
</style>
</head>
<body>

<header class="site-header">
  <div class="brand" style="left:235px;top:28px;font-size:25px;letter-spacing:-.5px"><span class="brand-box"></span>VELBRIC</div>
  <nav class="main-nav">
    <span class="active">HOME</span><span>SOLUTIONS</span><span>SERVICES</span><span>ABOUT US</span><span>CONTACT US</span>
  </nav>
  <div class="header-phone">
    <svg width="16" height="16" viewBox="0 0 24 24"><path fill="#0a8fd4" d="M6.6 10.8a15 15 0 0 0 6.6 6.6l2.2-2.2c.3-.3.7-.4 1-.2 1.1.4 2.3.6 3.6.6.6 0 1 .4 1 1V20c0 .6-.4 1-1 1C10.6 21 3 13.4 3 4c0-.6.4-1 1-1h3.5c.6 0 1 .4 1 1 0 1.3.2 2.5.6 3.6.1.3 0 .7-.2 1z"/></svg>
    (555) 014-2290
  </div>
</header>

<section class="hero">
  <svg class="abs" style="left:0;top:0" width="1200" height="472" viewBox="0 0 1200 472" role="img" aria-label="Photo of two colleagues working at a laptop, washed in pale blue">
    <defs><linearGradient id="heroBg" x1="0" x2="1"><stop offset="0" stop-color="#f1f8fd"/><stop offset=".55" stop-color="#e5f1fa"/><stop offset="1" stop-color="#d6e4ef"/></linearGradient></defs>
    <path d="M0 0H1200V395L600 471L0 395Z" fill="url(#heroBg)"/>
  </svg>
  <svg class="abs" style="left:0;top:0" width="1200" height="472" viewBox="0 0 1200 472">
    <path d="M325 82 A148.7 148.7 0 1 1 325 345" fill="none" stroke="#777" stroke-width="3"/>
    <circle cx="325" cy="82" r="6" fill="#0a8fd4"/>
    <circle cx="325" cy="345" r="6" fill="#0a8fd4"/>
    <g stroke="#0a8fd4" stroke-width="1.5" stroke-dasharray="2 3">
      <line x1="519" y1="125" x2="601" y2="125"/><line x1="549" y1="215" x2="630" y2="215"/><line x1="518" y1="304" x2="600" y2="304"/>
    </g>
    <circle cx="513" cy="125" r="6" fill="#fff" stroke="#0a8fd4" stroke-width="2"/>
    <circle cx="543" cy="215" r="6" fill="#fff" stroke="#0a8fd4" stroke-width="2"/>
    <circle cx="512" cy="304" r="6" fill="#fff" stroke="#0a8fd4" stroke-width="2"/>
  </svg>
  <div class="product-name"><i></i>tmPilot</div>
  <div class="hero-title">ENTERPRISE<br>CLIENT</div>

  <div class="feature-icon" style="left:601px;top:91px"><svg width="30" height="26" viewBox="0 0 30 26"><rect x="2" y="2" width="26" height="16" rx="3" fill="none" stroke="#fff" stroke-width="2"/><path d="M8 18 6 24 13 18" fill="none" stroke="#fff" stroke-width="2"/></svg></div>
  <div class="feature" style="left:681px;top:96px"><h3>80/20 Automation</h3><p>Automate repetitive inquiries and free up valuable time for your employees to focus on critical tasks</p></div>

  <div class="feature-icon" style="left:630px;top:181px"><svg width="24" height="30" viewBox="0 0 24 30"><rect x="2" y="2" width="20" height="26" rx="2" fill="none" stroke="#fff" stroke-width="2"/><path d="M6 9h12M6 14h12M6 19h8" stroke="#fff" stroke-width="2"/></svg></div>
  <div class="feature" style="left:708px;top:186px"><h3>Customer Experience</h3><p>Improve service quality by standardizing dialog flow and minimizing staff turnover and emotional agents.</p></div>

  <div class="feature-icon" style="left:600px;top:270px"><svg width="20" height="32" viewBox="0 0 20 32"><rect x="2" y="2" width="16" height="28" rx="3" fill="none" stroke="#fff" stroke-width="2"/><path d="M6 22v-4M10 22v-8M14 22v-11" stroke="#fff" stroke-width="2"/></svg></div>
  <div class="feature" style="left:681px;top:280px"><h3>Call Volume Agnostic</h3><p>tmPilot has the capacity to scale to handle spikes in call volume, able to handle virtually unlimited number of clients simultaneously</p></div>

  <div class="slider-dots"><i class="on"></i><i></i><i></i></div>
</section>

<section class="services">
  <div class="eyebrow" style="top:635px">SERVICES</div>
  <h2 class="section-title" style="top:660px">What We Do</h2>
  <p class="services-intro">Contract Staffing: At Velbric, our staff are readily available to deliver experienced and knowledgeable assistance to fill immediate or temporary needs for a diverse range of technologies and positions. Thus, we provide seasoned IT resources with a strong sense of business acumen to bring valuable experience and expertise to our clients to achieve reduced costs, greater efficiency and better services.</p>
  <svg class="abs" style="left:0;top:770px" width="1200" height="400" viewBox="0 0 1200 400">
    <g fill="none" stroke="#aaa" stroke-dasharray="4 3">
      <path d="M576 8 Q576 32 556 32 H368 V66"/>
      <path d="M624 8 Q624 32 644 32 H832 V66"/>
    </g>
    <path d="M367 66 L480 130 V255 L367 320 L254 255 V130Z" fill="#eaf5fc" stroke="#eaf5fc" stroke-width="12" stroke-linejoin="round"/>
    <path d="M832 66 L945 130 V255 L832 320 L719 255 V130Z" fill="#eaf5fc" stroke="#eaf5fc" stroke-width="12" stroke-linejoin="round"/>
  </svg>
  <div class="service-icon" style="left:340px;top:869px"></div>
  <div class="service-card" style="left:289px;top:943px"><h4>Digital Transformation</h4><ul><li>Process Automation via RPA and Conversational AI</li><li>Enterprise Application Integration</li></ul></div>
  <div class="center-mark">Velbric</div>
  <div class="service-icon" style="left:805px;top:869px"></div>
  <div class="service-card" style="left:754px;top:943px"><h4 style="text-align:center;width:152px">Network of Expertise</h4><ul><li>full-stack development,</li><li>from AI/ML, and data to legacy</li></ul></div>
</section>

<section class="testimonials" role="img" aria-label="Faint hexagon pattern on pale blue"></section>
<div class="eyebrow" style="top:1213px">TESTIMONIALS</div>
<h2 class="section-title" style="top:1238px">What Our Clients Are Saying</h2>
<article class="quote-card" style="left:234px">
  <div class="quote-mark">“</div>
  <p>“Naturally, the Travel Docs Bureau website receives thousands of visitors a day. As a result, we noticed the need to automate simple and repetitive questions to provide quick, on-demand assistance while maximizing our worker productivity without compromising costs. Thus, we enlisted Velbric Limited and their tmPilot solution to accomplish the task. Since launching the Travel Docs bot in Q4, 2019, we have achieved over 75% of inquiries being automatically answered successfully!”</p>
  <h5>Travel Docs Bureau</h5><div class="stars">★★★★★</div>
</article>
<article class="quote-card" style="left:610px">
  <div class="quote-mark">“</div>
  <p>“Leveraging tmPilot’s extremely user-friendly interface, Civic Help Office was able to build and implement our own bot for the My Civic Help Account (MCHA) page without the assistance of Velbric developers. By removing the need for programmers, we are able to make adjustments to our bot instantaneously!”</p>
  <h5>Civic Help Office</h5><div class="stars">★★★★★</div>
</article>
<div class="carousel-dots"><i class="on"></i><i></i><i></i><i></i></div>

<div class="video" role="img" aria-label="Video still of a smiling woman holding a tablet in a dim office">
  <div class="video-brand"><i></i>VELBRIC</div>
  <div class="video-action" style="left:578px"><svg width="16" height="16" viewBox="0 0 16 16" style="display:block;margin:0 auto 5px"><circle cx="8" cy="8" r="7" fill="#fff"/><path d="M8 4v4l3 2" stroke="#333" stroke-width="1.5" fill="none"/></svg>Watch later</div>
  <div class="video-action" style="left:640px"><svg width="16" height="16" viewBox="0 0 16 16" style="display:block;margin:0 auto 5px"><path d="M9 2l6 6-6 6V10C5 10 2 11 1 14 1 9 4 6 9 6z" fill="#fff"/></svg>Share</div>
  <div class="play"><svg width="52" height="40" viewBox="0 0 52 40"><path d="M21 12l12 8-12 8z" fill="#fff"/></svg></div>
</div>

<div class="divider-v"></div>
<h3 class="logo-block-title" style="left:222px;top:2246px">Our Clients</h3>
<h3 class="logo-block-title" style="left:598px;top:2246px">Our Partners</h3>
<div class="logo-name" style="left:283px;top:2318px">Teloria</div>
<div class="logo-name" style="left:408px;top:2318px">Paystead</div>
<div class="logo-name" style="left:315px;top:2390px">Nexora</div>
<div class="logo-name" style="left:424px;top:2390px">RoadAid</div>
<div class="logo-name" style="left:663px;top:2318px">Teloria</div>
<div class="logo-name" style="left:788px;top:2318px">Paystead</div>
<div class="logo-name" style="left:695px;top:2390px">Nexora</div>
<div class="logo-name" style="left:804px;top:2390px">RoadAid</div>

<footer class="site-footer">
  <svg class="abs" style="left:0;top:0" width="1200" height="355" viewBox="0 0 1200 355" role="img" aria-label="Pale blue footer backdrop with soft wave">
    <path d="M0 44 Q300 10 600 40 T1200 44 V355 H0Z" fill="#eef6fc"/>
  </svg>
</footer>
<div class="to-top"><svg width="34" height="34" viewBox="0 0 34 34"><path d="M12 19l5-5 5 5" stroke="#fff" stroke-width="2" fill="none"/></svg></div>
<div class="brand" style="left:235px;top:2597px;font-size:16px"><span class="brand-box" style="width:24px;height:24px;border-width:2px"></span>VELBRIC</div>
<p class="footer-about">Since 2011, the Velbric team has been providing professional IT services for major Canadian corporations operating in the telecommunications and financial sectors. As such, our team is highly skilled in technology integration, legacy modernization, system architecture design, application development, quality assurance, project management and more!</p>
<div class="footer-col" style="left:502px"><h6>QUICK LINKS</h6><ul style="margin-top:6px"><li>Home</li><li>Solutions</li><li>Services</li><li>About Us</li><li>Contact Us</li></ul></div>
<div class="footer-col" style="left:618px"><h6>CONTACT US</h6><p>41 Lakeview Road, Unit 7 &amp; 8 Northbrook,<br>ON Canada, A1B 2C3</p><p style="margin-top:6px">Phone: (555) 014-2290</p><p style="margin-top:6px">Email: info@velbriclimited.example</p></div>
<div class="footer-col social" style="left:841px"><h6>FOLLOW US</h6><ul style="margin-top:6px"><li><i></i>Chatterbox</li><li><i></i>Chirper</li><li><i></i>WorkLink</li></ul></div>
<div class="footer-rule"></div>
<p class="copyright">Copyrights © 2020 Velbric Limited. All rights reserved</p>

</body>
</html>
```